Daxholm APP redesign and color change

I am looking for a new design for my app. Please see the attached current design.

Currently, I have a functioning app but the colors and design are awful!
The logo is great but the rest of the app needs a refresh.
(Logo hi res not yet available but will upload soon.)
New colors or anything that is cutting edge.

Basically: It is a secure social media app within a school system where the teachers, students and parents can text, exchange photos, plan curriculum, etc.

I NEED ONLY landing page with a new look!
Looking for one distinct design for the landing page with new look.
The developer will apply this one design towards the rest of the pages/app screens.

Because part of the social media I need the feel and look of what is now the trend. Something that will attract and keep the client(s) interested. I am really leaving all the creative work to the designer and open to any suggestions.
Updates

Target Market(s)

Schools, community, teachers, students, colleges, sport teams

Industry/Entity Type

Non Profit

Font styles to use
Serif
Sans Serif

Colors

Designer to choose colors to be used in the design.

Requirements
Must have
• Sharp, trendy, millennial feel
Nice to have
• Up to designer
Should not have
• Up to designer

```html
<!DOCTYPE html>
<html lang="en">
<head>
<meta charset="utf-8">
<title>Daxholm – Conversation screen colour options</title>
<link rel="stylesheet" href="https://fonts.googleapis.com/css2?family=Montserrat:wght@400;500;600;800&display=swap">
<style>
  :root {
    --board-top: #4a4a4a;
    --board-bottom: #2b2b2b;
    --paper: #ffffff;
    --ink: #2e2e2e;
    --ink-soft: #4a4a4a;
    --ink-muted: #9a9a9a;
    --rule: #e6e6e6;
    --icon-grey: #6b6b6b;
    --teal: #12b5a2;
    --sky: #1eaaf1;
    --slate: #34495e;
    --sand: #e3b27f;
    --crimson: #c0334a;
    --rose: #f7305f;
    --coral: #f2706e;
    --lavender: #8a80e8;
  }
  * { box-sizing: border-box; margin: 0; padding: 0; }
  html, body { width: 1200px; height: 1200px; overflow: hidden; }
  body { font-family: "Montserrat", sans-serif; }
  .board {
    position: relative; width: 1200px; height: 1200px; overflow: hidden;
    background: radial-gradient(ellipse at 50% 20%, var(--board-top), var(--board-bottom) 80%);
  }
  .option { position: absolute; width: 272px; }
  .option-label {
    position: absolute; left: 0; right: 0; text-align: center;
    color: #fff; font-weight: 800; font-size: 40px; line-height: 1; top: -50px;
  }
  .row-1 { top: 101px; } .row-2 { top: 661px; }
  .col-1 { left: 27px; } .col-2 { left: 320px; } .col-3 { left: 613px; } .col-4 { left: 901px; }
  .row-1 .option-label { top: -49px; } .row-2 .option-label { top: -50px; }

  .theme-teal { --accent: var(--teal); --highlight: var(--teal); }
  .theme-sky { --accent: var(--sky); --highlight: var(--sky); }
  .theme-slate { --accent: var(--slate); --highlight: var(--ink); }
  .theme-sand { --accent: var(--sand); --highlight: var(--sand); }
  .theme-crimson { --accent: var(--crimson); --highlight: var(--crimson); }
  .theme-rose { --accent: var(--rose); --highlight: var(--rose); }
  .theme-coral { --accent: var(--coral); --highlight: var(--coral); }
  .theme-lavender { --accent: var(--lavender); --highlight: var(--lavender); }

  .phone { position: relative; width: 272px; height: 483px; background: var(--paper); overflow: hidden; }
  .appbar { position: relative; height: 54px; background: var(--accent); color: #fff; }
  .status {
    position: absolute; top: 1px; left: 12px; right: 10px; height: 11px;
    display: flex; justify-content: space-between; align-items: center; font-size: 9px; font-weight: 500;
  }
  .status-left, .status-right { display: flex; align-items: center; gap: 3px; width: 80px; }
  .status-right { justify-content: flex-end; }
  .status-time { font-weight: 600; }
  .signal { display: flex; gap: 1.5px; }
  .signal i { width: 4px; height: 4px; border-radius: 50%; background: #fff; display: block; }
  .signal i.off { background: none; border: 0.8px solid #fff; }
  .battery { width: 20px; height: 8px; background: #fff; border-radius: 1.5px; position: relative; }
  .battery::after { content: ""; position: absolute; right: -2px; top: 2.5px; width: 1.5px; height: 3px; background: #fff; }
  .appbar-title {
    position: absolute; top: 24px; left: 0; right: 0; text-align: center;
    font-size: 12.5px; font-weight: 600; letter-spacing: .1px;
  }
  .appbar-actions { position: absolute; right: 12px; top: 35px; display: flex; gap: 10px; }
  .appbar-actions svg { width: 15px; height: 15px; display: block; }

  .threads { list-style: none; padding-top: 2px; }
  .thread { position: relative; height: 59px; }
  .avatar {
    position: absolute; left: 14px; top: 6px; width: 46px; height: 46px; border-radius: 50%;
  }
  .avatar-a { background: radial-gradient(circle at 50% 40%, #c49476, #6e4a3a 70%); }
  .avatar-b { background: radial-gradient(circle at 50% 40%, #a67e66, #2f2522 70%); }
  .avatar-c { background: radial-gradient(circle at 50% 40%, #7a4f3c, #2a1c18 70%); }
  .avatar-d { background: radial-gradient(circle at 50% 40%, #b48a70, #3d2a22 70%); }
  .thread-body {
    position: absolute; left: 71px; right: 11px; top: 0; height: 59px; border-bottom: 1px solid var(--rule);
  }
  .thread:first-child .thread-body { height: 57px; }
  .thread-name { position: absolute; top: 14px; left: 0; font-size: 12.5px; font-weight: 500; color: var(--ink); }
  .unread .thread-name { color: var(--highlight); }
  .thread-preview { position: absolute; top: 33px; left: 0; font-size: 8px; color: var(--ink-soft); white-space: nowrap; }
  .thread-time { position: absolute; top: 22px; right: 0; font-size: 6px; color: var(--ink-muted); }
  .badge {
    position: absolute; top: 33px; right: 3px; width: 12px; height: 12px; border-radius: 50%;
    background: var(--accent); color: #fff; font-size: 7.5px; line-height: 12px; text-align: center;
  }

  .tabbar {
    position: absolute; left: 0; right: 0; bottom: 0; height: 33px;
    border-top: 1px solid var(--rule); box-shadow: 0 -1px 3px rgba(0,0,0,.05);
  }
  .tab { position: absolute; top: 6px; width: 20px; height: 20px; margin-left: -10px; }
  .tab svg { width: 20px; height: 20px; display: block; }
  .tab-chat { left: 30px; color: var(--accent); }
  .tab-board { left: 101px; color: var(--icon-grey); }
  .tab-contacts { left: 171px; color: var(--icon-grey); }
  .tab-settings { left: 241px; color: var(--icon-grey); }
</style>
</head>
<body>
<svg width="0" height="0" style="position:absolute" aria-hidden="true">
  <defs>
    <symbol id="icon-search" viewBox="0 0 16 16"><circle cx="6.5" cy="6.5" r="5" fill="none" stroke="#fff" stroke-width="1.6"/><path d="M10.2 10.2L15 15" stroke="#fff" stroke-width="1.6" stroke-linecap="round"/></symbol>
    <symbol id="icon-menu" viewBox="0 0 16 16"><path d="M1 3.5h14M1 8h14M1 12.5h14" stroke="#fff" stroke-width="1.5"/></symbol>
    <symbol id="icon-chat" viewBox="0 0 20 20"><path d="M8 2.5c3.6 0 6.5 2.3 6.5 5.2S11.6 13 8 13c-.7 0-1.4-.1-2-.3L2.5 14l1-2.6C2.3 10.5 1.5 9.2 1.5 7.7 1.5 4.8 4.4 2.5 8 2.5z" fill="none" stroke="currentColor" stroke-width="1.6"/><path d="M16 8.5c1.6.8 2.5 2.1 2.5 3.6 0 1.2-.6 2.3-1.6 3.1l.8 2.3-3-1.2c-.6.2-1.3.3-2 .3-2 0-3.7-.8-4.6-2" fill="none" stroke="currentColor" stroke-width="1.6"/></symbol>
    <symbol id="icon-board" viewBox="0 0 20 20"><g fill="currentColor"><rect x="2" y="2" width="7" height="7"/><rect x="11" y="2" width="7" height="7" fill="none" stroke="currentColor" stroke-width="1.2"/><rect x="2" y="11" width="3" height="3"/><rect x="6" y="11" width="3" height="3"/><rect x="2" y="15" width="3" height="3"/><rect x="6" y="15" width="3" height="3"/><path d="M11 18l7-7M11 14l3-3M15 18l3-3" stroke="currentColor" stroke-width="1.2"/></g></symbol>
    <symbol id="icon-contacts" viewBox="0 0 20 20"><rect x="4" y="2" width="12" height="16" rx="1" fill="currentColor"/><circle cx="10" cy="8.5" r="2.2" fill="#fff"/><path d="M6.5 14.5c.5-2 2-3 3.5-3s3 1 3.5 3z" fill="#fff"/></symbol>
    <symbol id="icon-gear" viewBox="0 0 20 20"><path fill="currentColor" d="M8.6 1h2.8l.5 2.4 1.6.7 2-1.3 2 2-1.3 2 .7 1.6 2.4.5v2.8l-2.4.5-.7 1.6 1.3 2-2 2-2-1.3-1.6.7-.5 2.4H8.6l-.5-2.4-1.6-.7-2 1.3-2-2 1.3-2-.7-1.6L.8 11.4V8.6l2.4-.5.7-1.6-1.3-2 2-2 2 1.3 1.6-.7z"/><circle cx="10" cy="10" r="3" fill="#fff"/></symbol>
  </defs>
</svg>

<main class="board">

  <!-- Option 1 -->
  <section class="option row-1 col-1 theme-teal">
    <h2 class="option-label">#1</h2>
    <div class="phone">
      <header class="appbar">
        <div class="status"><div class="status-left"><span class="signal"><i></i><i></i><i></i><i class="off"></i><i class="off"></i></span></div><span class="status-time">4:21 PM</span><div class="status-right"><span>100%</span><span class="battery"></span></div></div>
        <h1 class="appbar-title">Conversation</h1>
        <div class="appbar-actions"><svg><use href="#icon-search"/></svg><svg><use href="#icon-menu"/></svg></div>
      </header>
      <ul class="threads">
        <li class="thread unread"><div class="avatar avatar-a" role="img" aria-label="Profile photo of Milo Harker"></div><div class="thread-body"><span class="thread-name">Milo Harker</span><span class="thread-time">1 min ago</span><span class="thread-preview">Don't forget to finish your assigment this...</span><span class="badge">2</span></div></li>
        <li class="thread unread"><div class="avatar avatar-b" role="img" aria-label="Profile photo of Ravi Kandel"></div><div class="thread-body"><span class="thread-name">Ravi Kandel</span><span class="thread-time">5 min ago</span><span class="thread-preview">The Teacher-Parent Meeting is on next we...</span><span class="badge">2</span></div></li>
        <li class="thread"><div class="avatar avatar-c" role="img" aria-label="Profile photo of Tessa Dunmore"></div><div class="thread-body"><span class="thread-name">Tessa Dunmore</span><span class="thread-time">Yesterday</span><span class="thread-preview">Okay. see you in class!</span></div></li>
        <li class="thread"><div class="avatar avatar-d" role="img" aria-label="Profile photo of Joel Sutter"></div><div class="thread-body"><span class="thread-name">Joel Sutter</span><span class="thread-time">10/7/2017</span><span class="thread-preview">Have a nice weekend!</span></div></li>
      </ul>
      <nav class="tabbar"><span class="tab tab-chat"><svg><use href="#icon-chat"/></svg></span><span class="tab tab-board"><svg><use href="#icon-board"/></svg></span><span class="tab tab-contacts"><svg><use href="#icon-contacts"/></svg></span><span class="tab tab-settings"><svg><use href="#icon-gear"/></svg></span></nav>
    </div>
  </section>

  <!-- Option 2 -->
  <section class="option row-1 col-2 theme-sky">
    <h2 class="option-label">#2</h2>
    <div class="phone">
      <header class="appbar">
        <div class="status"><div class="status-left"><span class="signal"><i></i><i></i><i></i><i class="off"></i><i class="off"></i></span></div><span class="status-time">4:21 PM</span><div class="status-right"><span>100%</span><span class="battery"></span></div></div>
        <h1 class="appbar-title">Conversation</h1>
        <div class="appbar-actions"><svg><use href="#icon-search"/></svg><svg><use href="#icon-menu"/></svg></div>
      </header>
      <ul class="threads">
        <li class="thread unread"><div class="avatar avatar-a" role="img" aria-label="Profile photo of Milo Harker"></div><div class="thread-body"><span class="thread-name">Milo Harker</span><span class="thread-time">1 min ago</span><span class="thread-preview">Don't forget to finish your assigment this...</span><span class="badge">2</span></div></li>
        <li class="thread unread"><div class="avatar avatar-b" role="img" aria-label="Profile photo of Ravi Kandel"></div><div class="thread-body"><span class="thread-name">Ravi Kandel</span><span class="thread-time">5 min ago</span><span class="thread-preview">The Teacher-Parent Meeting is on next we...</span><span class="badge">2</span></div></li>
        <li class="thread"><div class="avatar avatar-c" role="img" aria-label="Profile photo of Tessa Dunmore"></div><div class="thread-body"><span class="thread-name">Tessa Dunmore</span><span class="thread-time">Yesterday</span><span class="thread-preview">Okay. see you in class!</span></div></li>
        <li class="thread"><div class="avatar avatar-d" role="img" aria-label="Profile photo of Joel Sutter"></div><div class="thread-body"><span class="thread-name">Joel Sutter</span><span class="thread-time">10/7/2017</span><span class="thread-preview">Have a nice weekend!</span></div></li>
      </ul>
      <nav class="tabbar"><span class="tab tab-chat"><svg><use href="#icon-chat"/></svg></span><span class="tab tab-board"><svg><use href="#icon-board"/></svg></span><span class="tab tab-contacts"><svg><use href="#icon-contacts"/></svg></span><span class="tab tab-settings"><svg><use href="#icon-gear"/></svg></span></nav>
    </div>
  </section>

  <!-- Option 3 -->
  <section class="option row-1 col-3 theme-slate">
    <h2 class="option-label">#3</h2>
    <div class="phone">
      <header class="appbar">
        <div class="status"><div class="status-left"><span class="signal"><i></i><i></i><i></i><i class="off"></i><i class="off"></i></span></div><span class="status-time">4:21 PM</span><div class="status-right"><span>100%</span><span class="battery"></span></div></div>
        <h1 class="appbar-title">Conversation</h1>
        <div class="appbar-actions"><svg><use href="#icon-search"/></svg><svg><use href="#icon-menu"/></svg></div>
      </header>
      <ul class="threads">
        <li class="thread unread"><div class="avatar avatar-a" role="img" aria-label="Profile photo of Milo Harker"></div><div class="thread-body"><span class="thread-name">Milo Harker</span><span class="thread-time">1 min ago</span><span class="thread-preview">Don't forget to finish your assigment this...</span><span class="badge">2</span></div></li>
        <li class="thread unread"><div class="avatar avatar-b" role="img" aria-label="Profile photo of Ravi Kandel"></div><div class="thread-body"><span class="thread-name">Ravi Kandel</span><span class="thread-time">5 min ago</span><span class="thread-preview">The Teacher-Parent Meeting is on next we...</span><span class="badge">2</span></div></li>
        <li class="thread"><div class="avatar avatar-c" role="img" aria-label="Profile photo of Tessa Dunmore"></div><div class="thread-body"><span class="thread-name">Tessa Dunmore</span><span class="thread-time">Yesterday</span><span class="thread-preview">Okay. see you in class!</span></div></li>
        <li class="thread"><div class="avatar avatar-d" role="img" aria-label="Profile photo of Joel Sutter"></div><div class="thread-body"><span class="thread-name">Joel Sutter</span><span class="thread-time">10/7/2017</span><span class="thread-preview">Have a nice weekend!</span></div></li>
      </ul>
      <nav class="tabbar"><span class="tab tab-chat"><svg><use href="#icon-chat"/></svg></span><span class="tab tab-board"><svg><use href="#icon-board"/></svg></span><span class="tab tab-contacts"><svg><use href="#icon-contacts"/></svg></span><span class="tab tab-settings"><svg><use href="#icon-gear"/></svg></span></nav>
    </div>
  </section>

  <!-- Option 4 -->
  <section class="option row-1 col-4 theme-sand">
    <h2 class="option-label">#4</h2>
    <div class="phone">
      <header class="appbar">
        <div class="status"><div class="status-left"><span class="signal"><i></i><i></i><i></i><i class="off"></i><i class="off"></i></span></div><span class="status-time">4:21 PM</span><div class="status-right"><span>100%</span><span class="battery"></span></div></div>
        <h1 class="appbar-title">Conversation</h1>
        <div class="appbar-actions"><svg><use href="#icon-search"/></svg><svg><use href="#icon-menu"/></svg></div>
      </header>
      <ul class="threads">
        <li class="thread unread"><div class="avatar avatar-a" role="img" aria-label="Profile photo of Milo Harker"></div><div class="thread-body"><span class="thread-name">Milo Harker</span><span class="thread-time">1 min ago</span><span class="thread-preview">Don't forget to finish your assigment this...</span><span class="badge">2</span></div></li>
        <li class="thread unread"><div class="avatar avatar-b" role="img" aria-label="Profile photo of Ravi Kandel"></div><div class="thread-body"><span class="thread-name">Ravi Kandel</span><span class="thread-time">5 min ago</span><span class="thread-preview">The Teacher-Parent Meeting is on next we...</span><span class="badge">2</span></div></li>
        <li class="thread"><div class="avatar avatar-c" role="img" aria-label="Profile photo of Tessa Dunmore"></div><div class="thread-body"><span class="thread-name">Tessa Dunmore</span><span class="thread-time">Yesterday</span><span class="thread-preview">Okay. see you in class!</span></div></li>
        <li class="thread"><div class="avatar avatar-d" role="img" aria-label="Profile photo of Joel Sutter"></div><div class="thread-body"><span class="thread-name">Joel Sutter</span><span class="thread-time">10/7/2017</span><span class="thread-preview">Have a nice weekend!</span></div></li>
      </ul>
      <nav class="tabbar"><span class="tab tab-chat"><svg><use href="#icon-chat"/></svg></span><span class="tab tab-board"><svg><use href="#icon-board"/></svg></span><span class="tab tab-contacts"><svg><use href="#icon-contacts"/></svg></span><span class="tab tab-settings"><svg><use href="#icon-gear"/></svg></span></nav>
    </div>
  </section>

  <!-- Option 5 -->
  <section class="option row-2 col-1 theme-crimson">
    <h2 class="option-label">#5</h2>
    <div class="phone">
      <header class="appbar">
        <div class="status"><div class="status-left"><span class="signal"><i></i><i></i><i></i><i class="off"></i><i class="off"></i></span></div><span class="status-time">4:21 PM</span><div class="status-right"><span>100%</span><span class="battery"></span></div></div>
        <h1 class="appbar-title">Conversation</h1>
        <div class="appbar-actions"><svg><use href="#icon-search"/></svg><svg><use href="#icon-menu"/></svg></div>
      </header>
      <ul class="threads">
        <li class="thread unread"><div class="avatar avatar-a" role="img" aria-label="Profile photo of Milo Harker"></div><div class="thread-body"><span class="thread-name">Milo Harker</span><span class="thread-time">1 min ago</span><span class="thread-preview">Don't forget to finish your assigment this...</span><span class="badge">2</span></div></li>
        <li class="thread unread"><div class="avatar avatar-b" role="img" aria-label="Profile photo of Ravi Kandel"></div><div class="thread-body"><span class="thread-name">Ravi Kandel</span><span class="thread-time">5 min ago</span><span class="thread-preview">The Teacher-Parent Meeting is on next we...</span><span class="badge">2</span></div></li>
        <li class="thread"><div class="avatar avatar-c" role="img" aria-label="Profile photo of Tessa Dunmore"></div><div class="thread-body"><span class="thread-name">Tessa Dunmore</span><span class="thread-time">Yesterday</span><span class="thread-preview">Okay. see you in class!</span></div></li>
        <li class="thread"><div class="avatar avatar-d" role="img" aria-label="Profile photo of Joel Sutter"></div><div class="thread-body"><span class="thread-name">Joel Sutter</span><span class="thread-time">10/7/2017</span><span class="thread-preview">Have a nice weekend!</span></div></li>
      </ul>
      <nav class="tabbar"><span class="tab tab-chat"><svg><use href="#icon-chat"/></svg></span><span class="tab tab-board"><svg><use href="#icon-board"/></svg></span><span class="tab tab-contacts"><svg><use href="#icon-contacts"/></svg></span><span class="tab tab-settings"><svg><use href="#icon-gear"/></svg></span></nav>
    </div>
  </section>

  <!-- Option 6 -->
  <section class="option row-2 col-2 theme-rose">
    <h2 class="option-label">#6</h2>
    <div class="phone">
      <header class="appbar">
        <div class="status"><div class="status-left"><span class="signal"><i></i><i></i><i></i><i class="off"></i><i class="off"></i></span></div><span class="status-time">4:21 PM</span><div class="status-right"><span>100%</span><span class="battery"></span></div></div>
        <h1 class="appbar-title">Conversation</h1>
        <div class="appbar-actions"><svg><use href="#icon-search"/></svg><svg><use href="#icon-menu"/></svg></div>
      </header>
      <ul class="threads">
        <li class="thread unread"><div class="avatar avatar-a" role="img" aria-label="Profile photo of Milo Harker"></div><div class="thread-body"><span class="thread-name">Milo Harker</span><span class="thread-time">1 min ago</span><span class="thread-preview">Don't forget to finish your assigment this...</span><span class="badge">2</span></div></li>
        <li class="thread unread"><div class="avatar avatar-b" role="img" aria-label="Profile photo of Ravi Kandel"></div><div class="thread-body"><span class="thread-name">Ravi Kandel</span><span class="thread-time">5 min ago</span><span class="thread-preview">The Teacher-Parent Meeting is on next we...</span><span class="badge">2</span></div></li>
        <li class="thread"><div class="avatar avatar-c" role="img" aria-label="Profile photo of Tessa Dunmore"></div><div class="thread-body"><span class="thread-name">Tessa Dunmore</span><span class="thread-time">Yesterday</span><span class="thread-preview">Okay. see you in class!</span></div></li>
        <li class="thread"><div class="avatar avatar-d" role="img" aria-label="Profile photo of Joel Sutter"></div><div class="thread-body"><span class="thread-name">Joel Sutter</span><span class="thread-time">10/7/2017</span><span class="thread-preview">Have a nice weekend!</span></div></li>
      </ul>
      <nav class="tabbar"><span class="tab tab-chat"><svg><use href="#icon-chat"/></svg></span><span class="tab tab-board"><svg><use href="#icon-board"/></svg></span><span class="tab tab-contacts"><svg><use href="#icon-contacts"/></svg></span><span class="tab tab-settings"><svg><use href="#icon-gear"/></svg></span></nav>
    </div>
  </section>

  <!-- Option 7 -->
  <section class="option row-2 col-3 theme-coral">
    <h2 class="option-label">#7</h2>
    <div class="phone">
      <header class="appbar">
        <div class="status"><div class="status-left"><span class="signal"><i></i><i></i><i></i><i class="off"></i><i class="off"></i></span></div><span class="status-time">4:21 PM</span><div class="status-right"><span>100%</span><span class="battery"></span></div></div>
        <h1 class="appbar-title">Conversation</h1>
        <div class="appbar-actions"><svg><use href="#icon-search"/></svg><svg><use href="#icon-menu"/></svg></div>
      </header>
      <ul class="threads">
        <li class="thread unread"><div class="avatar avatar-a" role="img" aria-label="Profile photo of Milo Harker"></div><div class="thread-body"><span class="thread-name">Milo Harker</span><span class="thread-time">1 min ago</span><span class="thread-preview">Don't forget to finish your assigment this...</span><span class="badge">2</span></div></li>
        <li class="thread unread"><div class="avatar avatar-b" role="img" aria-label="Profile photo of Ravi Kandel"></div><div class="thread-body"><span class="thread-name">Ravi Kandel</span><span class="thread-time">5 min ago</span><span class="thread-preview">The Teacher-Parent Meeting is on next we...</span><span class="badge">2</span></div></li>
        <li class="thread"><div class="avatar avatar-c" role="img" aria-label="Profile photo of Tessa Dunmore"></div><div class="thread-body"><span class="thread-name">Tessa Dunmore</span><span class="thread-time">Yesterday</span><span class="thread-preview">Okay. see you in class!</span></div></li>
        <li class="thread"><div class="avatar avatar-d" role="img" aria-label="Profile photo of Joel Sutter"></div><div class="thread-body"><span class="thread-name">Joel Sutter</span><span class="thread-time">10/7/2017</span><span class="thread-preview">Have a nice weekend!</span></div></li>
      </ul>
      <nav class="tabbar"><span class="tab tab-chat"><svg><use href="#icon-chat"/></svg></span><span class="tab tab-board"><svg><use href="#icon-board"/></svg></span><span class="tab tab-contacts"><svg><use href="#icon-contacts"/></svg></span><span class="tab tab-settings"><svg><use href="#icon-gear"/></svg></span></nav>
    </div>
  </section>

  <!-- Option 8 -->
  <section class="option row-2 col-4 theme-lavender">
    <h2 class="option-label">#8</h2>
    <div class="phone">
      <header class="appbar">
        <div class="status"><div class="status-left"><span class="signal"><i></i><i></i><i></i><i class="off"></i><i class="off"></i></span></div><span class="status-time">4:21 PM</span><div class="status-right"><span>100%</span><span class="battery"></span></div></div>
        <h1 class="appbar-title">Conversation</h1>
        <div class="appbar-actions"><svg><use href="#icon-search"/></svg><svg><use href="#icon-menu"/></svg></div>
      </header>
      <ul class="threads">
        <li class="thread unread"><div class="avatar avatar-a" role="img" aria-label="Profile photo of Milo Harker"></div><div class="thread-body"><span class="thread-name">Milo Harker</span><span class="thread-time">1 min ago</span><span class="thread-preview">Don't forget to finish your assigment this...</span><span class="badge">2</span></div></li>
        <li class="thread unread"><div class="avatar avatar-b" role="img" aria-label="Profile photo of Ravi Kandel"></div><div class="thread-body"><span class="thread-name">Ravi Kandel</span><span class="thread-time">5 min ago</span><span class="thread-preview">The Teacher-Parent Meeting is on next we...</span><span class="badge">2</span></div></li>
        <li class="thread"><div class="avatar avatar-c" role="img" aria-label="Profile photo of Tessa Dunmore"></div><div class="thread-body"><span class="thread-name">Tessa Dunmore</span><span class="thread-time">Yesterday</span><span class="thread-preview">Okay. see you in class!</span></div></li>
        <li class="thread"><div class="avatar avatar-d" role="img" aria-label="Profile photo of Joel Sutter"></div><div class="thread-body"><span class="thread-name">Joel Sutter</span><span class="thread-time">10/7/2017</span><span class="thread-preview">Have a nice weekend!</span></div></li>
      </ul>
      <nav class="tabbar"><span class="tab tab-chat"><svg><use href="#icon-chat"/></svg></span><span class="tab tab-board"><svg><use href="#icon-board"/></svg></span><span class="tab tab-contacts"><svg><use href="#icon-contacts"/></svg></span><span class="tab tab-settings"><svg><use href="#icon-gear"/></svg></span></nav>
    </div>
  </section>

</main>
</body>
</html>
```